Orbel Appraisals website redesign

I would like to refresh my existing website of www.orbelappraisals-demo.com with new graphics, look and feel, as well as updated structure and wording. Content and layout changes have been uploaded to this project Brief.

My existing website has a dark feel. I am now looking for a light and energetic feel. Financial Services is my industry, so the website should be reflect that. I would also like to reflect the concepts of Trust, Service and Expertise.

The website must be serious and upmarket.

Target Market(s)

Corporate board members, CFO's, treasurers and controllers
Auditors, tax advisors, private equity and venture capital asset managers, investors, tax authorities

Industry/Entity Type

Financial Service

Coding

Coded - Design and coding required

Number of Pages Required

5+ page

Font styles to use
Sans Serif
Other font styles liked:
• Designer can choose another modern font

Colors
0355a3
3277b5
85acd3
eaf1f7
f37122
f68d4d
9bcb3c
acd037
cadf82

Requirements
Must have
• Good hi resolution pictures that convey "Finance", "Trust", "Service" or "Expertise".
• An anti-bot (such as Captcha) mechanism in the contact form.
Should not have
• Must not have all content on one rolling screen.

```html
<!DOCTYPE html>
<html lang="en">
<head>
<meta charset="utf-8">
<title>Orbel Appraisals</title>
<link href="https://fonts.googleapis.com/css2?family=Marcellus+SC&family=Lato:wght@400;700&display=swap" rel="stylesheet">
<style>
:root{
  --orange:#f37122;
  --orange-soft:#f68d4d;
  --ink:#2f2f2f;
  --text:#555555;
  --muted:#777777;
  --line:#e6e6e6;
  --page:#f7f7f7;
  --white:#ffffff;
  --footer:#414141;
  --footer-bar:#efefef;
}
*{box-sizing:border-box;margin:0;padding:0}
html,body{width:1200px;height:2721px;overflow:hidden;background:var(--page)}
body{font-family:"Lato",sans-serif;color:var(--text)}
.canvas{position:relative;width:1200px;height:2721px;overflow:hidden;background:var(--page)}
.abs{position:absolute}
.caps{font-family:"Marcellus SC",serif;color:var(--ink);font-weight:400}

/* header */
.site-header{left:0;top:0;width:1200px;height:129px;background:var(--white)}
.brand{left:80px;top:30px;width:216px;height:74px;display:flex;align-items:center;gap:10px}
.brand-square{width:14px;height:14px;background:var(--orange)}
.brand-name{font-family:"Lato",sans-serif;font-weight:400;font-size:22px;color:#444}
.nav a{position:absolute;top:64px;font-size:13.5px;color:#333;text-decoration:none}
.nav a.active{color:var(--orange)}
.nav a.active::after{content:"";position:absolute;left:0;right:0;bottom:-8px;height:2px;background:var(--orange)}
.call{left:976px;top:56px;display:flex;align-items:center;gap:9px}
.call-icon{width:28px;height:28px;border-radius:50%;background:var(--orange);display:flex;align-items:center;justify-content:center}
.call-text{font-size:12.5px;line-height:15px;color:#333}
.call-text b{display:block;color:var(--orange);font-weight:400}

/* hero */
.hero{left:0;top:129px;width:1200px;height:566px;
  background:linear-gradient(100deg,#e4e4e4 0%,#cfcfcf 22%,#8e8e8e 45%,#6f6f6f 60%,#9b9384 78%,#c7b995 90%,#d8d2c4 100%)}
.hero-title{left:625px;top:212px;font-size:33px;line-height:38px;color:var(--white)}
.btn{display:flex;align-items:center;justify-content:center;background:var(--orange);color:var(--white);border-radius:22px;font-size:13.5px}
.hero-btn{left:624px;top:308px;width:163px;height:42px}
.dots span{position:absolute;left:1152px;width:8px;height:8px;border-radius:50%;background:#e8e8e8}
.dots span.on{background:var(--orange)}

/* about */
.about-title{left:0;width:1200px;top:722px;text-align:center;font-size:31px}
.swoosh{left:528px;top:770px}
.about-copy{left:226px;top:806px;width:752px;text-align:center;font-size:13.2px;line-height:16.3px;color:#444}
.about-copy p{margin-bottom:16px}
.about-btn{left:520px;top:991px;width:162px;height:42px}

/* services */
.service{width:326px;height:309px;background:var(--white);text-align:center}
.service-icon{position:absolute;left:118px;top:38px;width:90px;height:86px;border-radius:12px;
  background:radial-gradient(circle at 50% 45%,#fbd6bd 0%,#eeeeee 70%)}
.service h3{position:absolute;left:10px;right:10px;font-size:22.5px;line-height:28px}
.service p{position:absolute;left:28px;right:28px;font-size:13.2px;line-height:16.3px;color:#555}
.service .corner{position:absolute;right:6px;bottom:6px}
.service-lead{background:var(--orange);text-align:left}
.service-lead h2{position:absolute;left:36px;top:88px;font-size:37px;line-height:43px;color:var(--white)}
.service-lead p{position:absolute;left:36px;top:192px;width:262px;font-size:13.2px;line-height:16.3px;color:var(--white);font-weight:700}

/* news */
.news-band{left:0;top:1990px;width:1200px;height:372px;background:linear-gradient(180deg,rgba(247,247,247,0) 0%,#e3e6ea 35%,#d5d9de 100%)}
.news-title{left:0;width:1200px;top:1816px;text-align:center;font-size:31px}
.news-card{width:341px;height:361px;background:var(--white)}
.news-photo{position:absolute;left:11px;top:11px;width:319px;height:198px}
.date{position:absolute;left:11px;top:170px;width:41px;height:39px;background:#3d3d3d;color:var(--white);text-align:center;font-family:"Marcellus SC",serif;font-size:13px;line-height:14px;padding-top:6px}
.news-card h4{position:absolute;left:27px;top:244px;font-size:12.5px;color:#333}
.news-card p{position:absolute;left:26px;top:267px;width:300px;font-size:12.8px;line-height:16px;color:#555}
.news-card a{position:absolute;left:27px;top:327px;font-size:13.5px;color:#333;text-decoration:underline}
.view-btn{left:518px;top:2263px;width:163px;height:42px}

/* footer */
.site-footer{left:0;top:2362px;width:1200px;height:297px;background:var(--footer);color:#eee}
.foot-brand{left:79px;top:81px;width:245px;height:102px;border:2px solid #f2f2f2;display:flex;align-items:center;justify-content:center}
.foot-brand span{font-size:24px;color:#f2f2f2}
.foot-head{font-family:"Marcellus SC",serif;font-size:15px;color:#fff}
.foot-head::after{content:"";display:block;width:52px;height:2px;background:#eee;margin-top:10px}
.foot-list{list-style:none;font-size:13px}
.foot-list li{height:24px;position:relative;padding-left:19px}
.foot-list li::before{content:"";position:absolute;left:0;top:7px;width:4px;height:4px;border-radius:50%;background:#eee}
.contact-list{list-style:none;font-size:13px}
.contact-list li{height:24px;position:relative;padding-left:30px}
.contact-list svg{position:absolute;left:0;top:2px}
.field{position:absolute;border:1px solid #cfcfcf;font-size:12.5px;color:#eee;padding:7px 9px;letter-spacing:.5px}
.send{left:856px;top:213px;width:167px;height:38px;font-size:13px;letter-spacing:.5px}
.footer-bar{left:0;top:2659px;width:1200px;height:62px;background:var(--footer-bar)}
.copyright{left:79px;top:21px;font-size:14px;color:#333}
.social span{position:absolute;top:14px;width:34px;height:34px;border-radius:50%;border:1.5px solid #777}
.social span.on{background:var(--orange);border-color:var(--orange)}
</style>
</head>
<body>
<div class="canvas">

  <header class="site-header abs">
    <div class="brand abs"><span class="brand-square"></span><span class="brand-name">Orbel Appraisals</span></div>
    <nav class="nav">
      <a class="active" style="left:525px">Home</a>
      <a style="left:609px">About</a>
      <a style="left:694px">Services <small>v</small></a>
      <a style="left:793px">News</a>
      <a style="left:875px">Contact</a>
    </nav>
    <div class="call abs">
      <span class="call-icon">
        <svg width="14" height="14" viewBox="0 0 24 24"><path fill="#fff" d="M6.6 10.8c1.4 2.8 3.8 5.1 6.6 6.6l2.2-2.2c.3-.3.7-.4 1-.2 1.1.4 2.3.6 3.6.6.6 0 1 .4 1 1V20c0 .6-.4 1-1 1C10.6 21 3 13.4 3 4c0-.6.4-1 1-1h3.5c.6 0 1 .4 1 1 0 1.3.2 2.5.6 3.6.1.3 0 .7-.2 1z"/></svg>
      </span>
      <div class="call-text"><b>Call Us Now</b>+31 70 555 0148</div>
    </div>
  </header>

  <section class="hero abs" role="img" aria-label="Photo of a small model house, a toy car and stacks of gold coins on paperwork while a businessman writes">
    <h1 class="hero-title caps abs" style="color:#fff">Business &amp; Intellectual<br>Property Valuations</h1>
    <div class="btn hero-btn abs">Read More</div>
    <div class="dots">
      <span style="top:219px"></span><span class="on" style="top:235px"></span><span style="top:252px"></span><span style="top:269px"></span>
    </div>
  </section>

  <h2 class="about-title caps abs">About us</h2>
  <svg class="swoosh abs" width="144" height="14" viewBox="0 0 144 14"><path d="M2 9 C40 2,90 2,142 8 C95 5,50 6,2 9Z" fill="#333"/></svg>
  <div class="about-copy abs">
    <p>Orbel Appraisals, founded in 2012, is a boutique corporate finance practice servicing companies throughout Europe and North America. Our office is located in the Netherland in the Linden Science Park. Our clients come from a broad range of industries with valuations ranging between micro-cap and large-cap.</p>
    <p>Orbel Appraisals assists companies with valuations of businesses and intellectual property, M&amp;A advisory, business plan coaching and purchase price allocation (PPA). Through our bespoke approach and global network, we customize teams to the needs of our clients.</p>
    <p>Trust, Service and Expertise are the 3 pillars of Orbel Appraisals. Trust is paramount.<br>Clients rely on Orbel Appraisals Services...</p>
  </div>
  <div class="btn about-btn abs">Read More</div>

  <!-- services -->
  <div class="service service-lead abs" style="left:79px;top:1099px">
    <h2 class="caps">Our<br>Services</h2>
    <p>Lorem Ipsum is simply dummy text of the printing and typesetting industry. Lorem has been the industry's standard dummy text ever since the 1500s,</p>
  </div>

  <div class="service abs" style="left:436px;top:1099px">
    <div class="service-icon" role="img" aria-label="Icon of a hand holding a dollar coin with a rising chart"></div>
    <h3 class="caps" style="top:146px">Business Valuation</h3>
    <p style="top:186px">Lorem Ipsum is simply dummy text of the printing and typesetting industry. Lorem has been the industry's standard dummy text ever since the 1500s,</p>
    <svg class="corner" width="62" height="58"><polygon points="62,0 62,58 0,58" fill="var(--orange)"/><path d="M44 33v16M36 41h16" stroke="#fff" stroke-width="2"/></svg>
  </div>

  <div class="service abs" style="left:793px;top:1099px">
    <div class="service-icon" role="img" aria-label="Icon of gears beside a balance scale"></div>
    <h3 class="caps" style="top:146px">Intellectual Property<br>Valuation</h3>
    <p style="top:206px">Lorem Ipsum is simply dummy text of the printing and typesetting industry. Lorem has been the industry's standard dummy text ever since the 1500s,</p>
    <svg class="corner" width="62" height="58"><polygon points="62,0 62,58 0,58" fill="var(--orange)"/><path d="M44 33v16M36 41h16" stroke="#fff" stroke-width="2"/></svg>
  </div>

  <div class="service abs" style="left:79px;top:1436px">
    <div class="service-icon" role="img" aria-label="Icon of a plan document with a flow diagram"></div>
    <h3 class="caps" style="top:138px">Business Plan<br>Coaching</h3>
    <p style="top:189px">Lorem Ipsum is simply dummy text of the printing and typesetting industry. Lorem has been the industry's standard dummy text ever since the 1500s,</p>
    <svg class="corner" width="62" height="58"><polygon points="62,0 62,58 0,58" fill="var(--orange)"/><path d="M44 33v16M36 41h16" stroke="#fff" stroke-width="2"/></svg>
  </div>

  <div class="service abs" style="left:436px;top:1436px">
    <div class="service-icon" role="img" aria-label="Icon of two advisors with a speech bubble"></div>
    <h3 class="caps" style="top:150px">M&amp;A Advisory</h3>
    <p style="top:189px">Lorem Ipsum is simply dummy text of the printing and typesetting industry. Lorem has been the industry's standard dummy text ever since the 1500s,</p>
    <svg class="corner" width="62" height="58"><polygon points="62,0 62,58 0,58" fill="var(--orange)"/><path d="M44 33v16M36 41h16" stroke="#fff" stroke-width="2"/></svg>
  </div>

  <div class="service abs" style="left:793px;top:1436px">
    <div class="service-icon" role="img" aria-label="Icon of a pie chart with a dollar sign"></div>
    <h3 class="caps" style="top:136px">Purchase Price<br>Allocation</h3>
    <p style="top:190px">Lorem Ipsum is simply dummy text of the printing and typesetting industry. Lorem has been the industry's standard dummy text ever since the 1500s,</p>
    <svg class="corner" width="62" height="58"><polygon points="62,0 62,58 0,58" fill="var(--orange)"/><path d="M44 33v16M36 41h16" stroke="#fff" stroke-width="2"/></svg>
  </div>

  <!-- news -->
  <div class="news-band abs" role="img" aria-label="Faded city skyline behind the news section"></div>
  <h2 class="news-title caps abs">Latest News</h2>

  <article class="news-card abs" style="left:69px;top:1870px">
    <div class="news-photo" role="img" aria-label="Photo of a businessman cheering at his laptop while holding a report" style="background:linear-gradient(120deg,#eef0ee,#d8dcd6 45%,#5b5b5e 70%,#e7e7e7)"></div>
    <div class="date">02<br>Oct</div>
    <h4 class="caps">What is Lorem Ipsum?</h4>
    <p>Lorem ipsum dolor sit amet, consectetur adipiscing elit, sed do eiusmod tempor incididunt ut labore et dolore magna aliqua.</p>
    <a>Read More</a>
  </article>

  <article class="news-card abs" style="left:426px;top:1870px">
    <div class="news-photo" role="img" aria-label="Photo of a hand using a tablet showing financial charts" style="background:linear-gradient(135deg,#2e4a66,#5d7f9e 45%,#a9c3da 75%,#dfe9f2)"></div>
    <div class="date">02<br>Oct</div>
    <h4 class="caps">What is Lorem Ipsum?</h4>
    <p>Lorem Ipsum is simply dummy the printing and typesetting industry. Lorem Ipsum has been the standard dummy.</p>
    <a>Read More</a>
  </article>

  <article class="news-card abs" style="left:787px;top:1870px">
    <div class="news-photo" role="img" aria-label="Photo of two colleagues reviewing documents at an office desk" style="background:linear-gradient(120deg,#dfe4e6,#9eb3c6 40%,#3f5a86 65%,#c9d3da)"></div>
    <div class="date">02<br>Oct</div>
    <h4 class="caps">What is Lorem Ipsum?</h4>
    <p>Lorem Ipsum is simply dummy the printing and typesetting industry. Lorem Ipsum has been the standard dummy.</p>
    <a>Read More</a>
  </article>

  <div class="btn view-btn abs">View More</div>

  <!-- footer -->
  <footer class="site-footer abs">
    <div class="foot-brand abs"><span>Orbel Appraisals</span></div>

    <div class="abs" style="left:439px;top:58px">
      <div class="foot-head">Quick Link</div>
      <ul class="foot-list" style="margin-top:20px">
        <li>Home</li><li>About</li><li>Services</li><li>News</li><li>Contact</li>
      </ul>
    </div>

    <div class="abs" style="left:620px;top:58px">
      <div class="foot-head">Quick Contact</div>
      <ul class="contact-list" style="margin-top:20px">
        <li><svg width="14" height="14" viewBox="0 0 24 24"><path d="M12 2a7 7 0 0 0-7 7c0 5 7 13 7 13s7-8 7-13a7 7 0 0 0-7-7zm0 9.5A2.5 2.5 0 1 1 12 6.5a2.5 2.5 0 0 1 0 5z" fill="none" stroke="#ddd" stroke-width="1.6"/></svg>Veldzichtlaan 27</li>
        <li>2301 XK Leiden</li>
        <li>The Netherlands</li>
        <li><svg width="16" height="14" viewBox="0 0 24 20"><path d="M3 7c5-4 13-4 18 0l-3 3-3-2v-2H9v2l-3 2zM6 12h12l2 6H4z" fill="none" stroke="#ddd" stroke-width="1.5"/></svg>+31 70 555 0148</li>
        <li><svg width="15" height="12" viewBox="0 0 24 18"><rect x="1" y="1" width="22" height="16" fill="none" stroke="#ddd" stroke-width="1.6"/><path d="M1 1l11 9 11-9" fill="none" stroke="#ddd" stroke-width="1.6"/></svg>info@orbel-demo.com</li>
      </ul>
    </div>

    <div class="abs" style="left:856px;top:58px">
      <div class="foot-head">Contact Us</div>
    </div>
    <div class="field" style="left:856px;top:110px;width:126px;height:32px">Name</div>
    <div class="field" style="left:990px;top:110px;width:126px;height:32px">Phone</div>
    <div class="field" style="left:856px;top:151px;width:260px;height:55px">Message</div>
    <div class="btn send abs">Send</div>
  </footer>

  <div class="footer-bar abs">
    <div class="copyright abs">Copyright © 2019 Orbel Appraisals. All Right Reserve</div>
    <div class="social">
      <span class="on" style="left:943px"></span>
      <span style="left:990px"></span>
      <span style="left:1037px"></span>
      <span style="left:1083px"></span>
    </div>
  </div>

</div>
</body>
</html>
```